Independence Day/4th of July Illustration

Marlowe Crest is in need of an illustration to be used in an Independence Day/4th of July-themed email to clients. We would like our company logo incorporated into the illustration, along with the text “Have a Marlowe Crest 4th!”

Must be 600px wide, maximum 300px tall. An eps file is preferred. Company logo is provided.

It Company

Sans Serif

```html
<!DOCTYPE html>
<html lang="en">
<head>
<meta charset="utf-8">
<title>Have a Marlowe Crest 4th!</title>
<link rel="stylesheet" href="https://fonts.googleapis.com/css2?family=Rammetto+One&display=swap">
<style>
  :root {
    --bg-center: #a3161c;
    --bg-edge: #4c0507;
    --flag-navy: #1f2d6b;
    --flag-blue: #34468f;
    --flag-white: #f4efe6;
    --flag-red: #c8192b;
    --outline: #0b0b0b;
    --brand-red: #e0202a;
  }
  * { margin: 0; padding: 0; box-sizing: border-box; }
  html, body { width: 1200px; height: 600px; overflow: hidden; }
  body { font-family: "Rammetto One", "Arial Black", sans-serif; }

  .greeting-card {
    position: relative;
    width: 1200px;
    height: 600px;
    overflow: hidden;
    background: radial-gradient(ellipse at 45% 45%, var(--bg-center) 0%, #7e0d11 55%, var(--bg-edge) 100%);
  }

  .headline { position: absolute; left: 18px; top: 0; }

  .headline-line {
    display: block;
    white-space: nowrap;
    line-height: 1;
    color: transparent;
    background: linear-gradient(172deg,
      var(--flag-navy) 0%, var(--flag-blue) 28%,
      var(--flag-white) 42%, var(--flag-red) 58%,
      var(--flag-white) 74%, var(--flag-red) 92%);
    -webkit-background-clip: text;
    background-clip: text;
    -webkit-text-stroke: 4px var(--outline);
    filter: drop-shadow(6px 8px 4px rgba(0, 0, 0, 0.7));
    position: absolute;
    left: 0;
  }

  .line-have { top: 4px; font-size: 128px; }
  .line-name { top: 140px; font-size: 170px; letter-spacing: -2px; }
  .line-closing { top: 350px; }
  .closing-word { font-size: 122px; vertical-align: baseline; }
  .closing-day { font-size: 200px; margin-left: 24px; }

  .brand-signoff {
    position: absolute;
    right: 58px;
    bottom: 58px;
    display: flex;
    flex-direction: column;
    align-items: center;
    gap: 14px;
  }
  .brand-dot { display: block; }
  .brand-name {
    font-size: 26px;
    color: var(--brand-red);
    white-space: nowrap;
  }
</style>
</head>
<body>
  <main class="greeting-card">
    <h1 class="headline" aria-label="Have a Marlowe Crest 4th!">
      <span class="headline-line line-have">Have a</span>
      <span class="headline-line line-name">Marlowe</span>
      <span class="headline-line line-closing"><span class="closing-word">Crest</span><span class="closing-day">4th</span></span>
    </h1>

    <footer class="brand-signoff">
      <svg class="brand-dot" width="92" height="92" viewBox="0 0 92 92" aria-hidden="true">
        <circle cx="46" cy="46" r="44" fill="var(--brand-red)"/>
      </svg>
      <span class="brand-name">Marlowe Crest</span>
    </footer>
  </main>
</body>
</html>
```